BrightLoop (1 page) homepage re-design

Our homepage needs a face-lift! We need our homepage on our website re-designed with a fresh and current look and feel. We have all the details, colour codes and a rough wireframe ready, but need a talented designer to put some personality into our ideas.

What we do: BrightLoop is a digital marketing agency with offices in Australia (Sydney) and South Africa (Cape Town). We specialise in SEO, PPC (otherwise known as Zentro PayLine or SEM), content marketing and Zentro Tallyboard. We use these tools to help our clients realise their business dreams.

VISUAL

Style / theme of the design:
Clean, simplistic, fun, flow.

Websites we draw inspiration from:
This is the theme we want to use to build the website
http://demo.vormalayouts.example/vl/?theme=Pebbled
Inspiration:
https://www.ondrapromo.example/
https://www.nelvagrowth.example.au/
https://quimbel.example.au/
https://torvin.layout-works.example/forum/

What we like about the site:
Clean, simple design, good use of white space. The subtle changing background colours, strong contrast with text. Not too busy or distracting.

What we don’t want: Too many different colours.

Target Market(s)

Our target audience: Marketing Managers of small to medium size businesses in Australia.

Industry/Entity Type

Marketing

Number of Pages Required

1 page

Font styles to use
Sans Serif

Requirements
Must have
• Elements to be added on homepage in order and as seen in attachments:
• - Section 1: Video with team as image and a play button add the heading: We help smart marketing managers achieve their KPIs [line break] and reduce their digital marketing overwhelm.
• - Section 2: Solutions section with the 6 solutions displayed in a row.
• - Section 3: Register Free Webinar with video
• - Section 4: Please add 3 case studies (as seen in attached docs there is only 1 but please add 3 below each other)
• - Section 5: Clients. Please add all client logo’s (black and white)
• - Section 6: Our Blog (as seen attached)
• - Section 7: Conferences Attended (please add the title and a paragraph of lorem Ipsom below) and then please add all conference logo’s attached below.
• - Section 8: In The Media (please add all logo’s titled media) white background
• - Section 9: Footer (dark grey footer) add our Zentro honoured affiliate logo here please
• - Section10: Footer - include:
• - Social logos (WorkMesh, Blipster, Pallwall, ReelDrop, Zentro Hub)
• - Navigation
• - Contact details (name, address, phone number, email)
• Colour codes:
• We want to use light greys, white and charcoal grey for the backgrounds with a pop of our green colour to bring out our branding and all CTA’s to be orange, colour codes below:
• Light grey: #F2F2F2
• Charcoal grey: #161616
• Green: #428E29
• CTA’s: #de7532
• PLEASE NOTE: Please see attached pdf titled: homepagecopybrief.pdf for all the titles and statistics that need to go on the homepage
Should not have
• Too much colour, icons should not be different colours

```html
<!DOCTYPE html>
<html lang="en">
<head>
<meta charset="utf-8">
<title>BrightLoop – Digital Marketing</title>
<link href="https://fonts.googleapis.com/css2?family=Arimo:wght@400;700&display=swap" rel="stylesheet">
<style>
  :root {
    --green: #0b8e0b;
    --ink: #111111;
    --text: #1d1d1d;
    --white: #ffffff;
    --bar: #000000;
    --hero-dark: #2b2b2d;
    --hero-mid: #4a4a4e;
  }
  * { margin: 0; padding: 0; box-sizing: border-box; }
  html, body {
    width: 1200px; height: 1200px; overflow: hidden;
    background: var(--white);
    font-family: "Arimo", Arial, sans-serif;
    color: var(--text);
  }
  .page { position: relative; width: 1200px; height: 1200px; }

  .topbar {
    position: absolute; left: 162px; top: 0; width: 919px; height: 17px;
    background: var(--bar); color: var(--white); font-size: 9.5px;
  }
  .topbar-item { position: absolute; top: 2px; display: flex; align-items: center; gap: 6px; }
  .topbar-item svg { width: 9px; height: 10px; fill: var(--white); }
  .topbar-address { left: 582px; }
  .topbar-phone { left: 830px; }

  .hero {
    position: absolute; left: 162px; top: 17px; width: 919px; height: 534px;
    overflow: hidden;
  }
  .hero-photo {
    position: absolute; inset: 0;
    background: linear-gradient(180deg, var(--hero-mid) 0%, var(--hero-dark) 45%, #1c1c22 100%);
  }
  .brand {
    position: absolute; left: 11px; top: 10px;
    display: flex; align-items: center; gap: 7px;
  }
  .brand-mark { width: 18px; height: 18px; background: var(--green); }
  .brand-name {
    font-size: 17px; font-weight: 400; letter-spacing: 3px;
    color: var(--white); text-transform: uppercase;
  }
  .menu {
    position: absolute; right: 8px; top: 9px;
    display: flex; align-items: center; gap: 10px;
    color: var(--white); font-size: 14px;
  }
  .menu-button {
    width: 40px; height: 24px; background: var(--white);
    display: flex; flex-direction: column; justify-content: center; align-items: center; gap: 3px;
  }
  .menu-button span { display: block; width: 28px; height: 2.5px; background: var(--ink); }
  .hero-heading {
    position: absolute; left: 88px; top: 350px; width: 800px;
    color: var(--white); font-size: 24px; font-weight: 400; line-height: 28px;
    text-transform: uppercase;
  }
  .hero-cta {
    position: absolute; left: 88px; top: 431px; width: 134px; height: 42px;
    background: var(--white); color: var(--green);
    font-size: 13px; line-height: 42px; padding-left: 9px; text-transform: uppercase;
  }

  .solution { position: absolute; left: 171px; top: 590px; width: 900px; }
  .section-title { font-size: 23.5px; font-weight: 400; color: var(--ink); text-transform: uppercase; }
  .section-rule { width: 135px; height: 5px; background: var(--green); margin-top: 9px; }
  .section-intro { font-size: 14.4px; line-height: 18.5px; margin-top: 10px; width: 900px; }

  .feature { position: absolute; width: 285px; }
  .feature-icon { display: block; fill: var(--green); }
  .feature-title {
    font-size: 17.6px; font-weight: 400; color: var(--ink);
    line-height: 22px; text-transform: uppercase; margin-top: 14px;
  }
  .feature-text { font-size: 14.4px; line-height: 18.5px; margin-top: 3px; }
</style>
</head>
<body>
<div class="page">

  <div class="topbar">
    <div class="topbar-item topbar-address">
      <svg viewBox="0 0 10 12"><path d="M5 0C2.5 0 .8 1.8.8 4.1 .8 7 5 12 5 12s4.2-5 4.2-7.9C9.2 1.8 7.5 0 5 0zm0 5.7a1.6 1.6 0 110-3.2 1.6 1.6 0 010 3.2z"/></svg>
      <span>24-26 Harbourline St, Millers Point, Sydney</span>
    </div>
    <div class="topbar-item topbar-phone">
      <svg viewBox="0 0 12 12"><path d="M2.4 0l2 2.6-1.1 1.6c.8 1.7 2.2 3.1 3.9 3.9l1.6-1.1L11.4 9 10 11.6C4.6 11.3.6 7.1.4 1.6z"/></svg>
      <span>1300 000 412</span>
    </div>
  </div>

  <header class="hero">
    <div class="hero-photo" role="img" aria-label="Team photo: eight smiling BrightLoop staff standing together in front of a dark grey wall"></div>
    <div class="brand">
      <span class="brand-mark"></span>
      <span class="brand-name">BrightLoop</span>
    </div>
    <div class="menu">
      <span>MENU</span>
      <div class="menu-button"><span></span><span></span><span></span></div>
    </div>
    <h1 class="hero-heading">We help smart marketing managers achieve their KPIs<br>and reduce their digital marketing overwhelm.</h1>
    <div class="hero-cta">Read more...</div>
  </header>

  <section class="solution">
    <h2 class="section-title">Solution</h2>
    <div class="section-rule"></div>
    <p class="section-intro">Lorem ipsum dolor sit amet, mattis gravida, vestibulum curabitur, ante pellentesque, sit lacinia mauris pulvinar ut. Morbi rutrum laoreet sit ipsum venenatis proin, cursus hendrerit quis, tellus scelerisque, ac amet commodo tincidunt. Lorem metus. In lectus justo, urna dis, in eu nullam sem urna sociis.</p>
  </section>

  <div class="feature" style="left:171px; top:740px;">
    <svg class="feature-icon" width="78" height="68" viewBox="0 0 78 68">
      <rect x="10" y="50" width="9" height="18"/><rect x="24" y="40" width="9" height="28"/>
      <rect x="38" y="44" width="9" height="24"/><rect x="52" y="28" width="9" height="40"/>
      <path d="M0 60 L24 34 L38 44 L62 16 L56 10 L78 0 L74 22 L68 16 L39 52 L25 42 L6 64Z"/>
    </svg>
    <h3 class="feature-title">Growth Revenue</h3>
    <p class="feature-text">Lorem ipsum dolor sit amet, mattis gravi-da, vestibulum curabitur, ante pellen-tesque, ac amet commodo tincidunts, in eu nullam sem urna sociis.</p>
  </div>

  <div class="feature" style="left:478px; top:740px;">
    <svg class="feature-icon" width="78" height="68" viewBox="0 0 78 68">
      <circle cx="14" cy="8" r="7"/><circle cx="48" cy="8" r="7"/>
      <path d="M2 56c0-10 5-16 12-16h4v16z"/><path d="M62 40h-2v10l4 4c0-7-1-12-2-14z"/>
      <circle cx="38" cy="34" r="18" fill="none" stroke="#0b8e0b" stroke-width="5"/>
      <circle cx="38" cy="29" r="6"/><path d="M28 44c1-6 5-8 10-8s9 2 10 8z"/>
      <path d="M50 48l6-6 18 18-6 6z"/>
    </svg>
    <h3 class="feature-title">Convert Leads</h3>
    <p class="feature-text">Lorem ipsum dolor sit amet, mattis gravida, vestibulum curabitur, ante pellentesque, ac amet commodo tincidunts, in eu nullam sem urna sociis.</p>
  </div>

  <div class="feature" style="left:795px; top:740px;">
    <svg class="feature-icon" width="78" height="68" viewBox="0 0 78 68">
      <rect x="2" y="22" width="16" height="22"/>
      <path d="M18 22 L38 10 V56 L18 44Z"/><circle cx="40" cy="33" r="4"/>
      <path d="M46 22a14 14 0 010 22" fill="none" stroke="#0b8e0b" stroke-width="4"/>
      <path d="M53 14a24 24 0 010 38" fill="none" stroke="#0b8e0b" stroke-width="4"/>
      <path d="M60 6a34 34 0 010 54" fill="none" stroke="#0b8e0b" stroke-width="4"/>
    </svg>
    <h3 class="feature-title">Increase Brand<br>Awareness</h3>
    <p class="feature-text">Lorem ipsum dolor sit amet, mattis gravida, vestibulum curabitur, ante pel-lentesque, ac amet commodo tincid-unts, in eu nullam sem urna sociis.</p>
  </div>

  <div class="feature" style="left:171px; top:979px;">
    <svg class="feature-icon" width="78" height="66" viewBox="0 0 78 66">
      <ellipse cx="28" cy="9" rx="27" ry="9"/>
      <path d="M1 15c0 5 12 9 27 9s27-4 27-9v10c0 5-12 9-27 9S1 30 1 25z"/>
      <path d="M1 31c0 5 12 9 27 9 4 0 8 0 11-1v9c-3 1-7 1-11 1C13 49 1 45 1 40z"/>
      <path d="M1 46c0 5 12 9 27 9 4 0 8 0 11-1v8c-3 1-7 1-11 1C13 63 1 59 1 54z"/>
      <circle cx="60" cy="48" r="10"/>
      <g stroke="#0b8e0b" stroke-width="5"><path d="M60 34v28M46 48h28M50 38l20 20M70 38L50 58"/></g>
      <circle cx="60" cy="48" r="4" fill="#fff"/>
    </svg>
    <h3 class="feature-title">Data IKPI’s</h3>
    <p class="feature-text">Lorem ipsum dolor sit amet, mattis gravi-da, vestibulum curabitur, ante pellen-tesque, ac amet commodo tincidunts, in eu nullam sem urna sociis.</p>
  </div>

  <div class="feature" style="left:478px; top:979px;">
    <svg class="feature-icon" width="78" height="66" viewBox="0 0 78 66">
      <path d="M0 40h24v5H0zM9.5 30h5v25h-5z"/>
      <circle cx="42" cy="28" r="10"/><path d="M24 62c0-12 8-19 18-19s18 7 18 19z"/>
      <circle cx="62" cy="32" r="7"/><path d="M58 44c10 0 15 6 16 18H63c0-8-2-13-5-18z"/>
    </svg>
    <h3 class="feature-title">Increase Engagement</h3>
    <p class="feature-text">Lorem ipsum dolor sit amet, mattis gravida, vestibulum curabitur, ante pellentesque, ac amet commodo tincidunts, in eu nullam sem urna sociis.</p>
  </div>

  <div class="feature" style="left:795px; top:979px;">
    <svg class="feature-icon" width="78" height="66" viewBox="0 0 78 66">
      <circle cx="33" cy="33" r="32"/>
      <circle cx="33" cy="33" r="24" fill="#fff"/>
      <circle cx="33" cy="33" r="18"/>
      <circle cx="33" cy="33" r="11" fill="#fff"/>
      <circle cx="33" cy="33" r="6"/>
      <path d="M33 33L52 14" stroke="#fff" stroke-width="3"/>
      <path d="M49 12l6-6 1 6 6 1-6 6z" fill="#fff"/>
    </svg>
    <h3 class="feature-title">Marketing Strategy<br>Budgeting</h3>
    <p class="feature-text">Lorem ipsum dolor sit amet, mattis gravida, vestibulum curabitur, ante pell Register For Your Free Webinar en-tesque, ac amet commodo tincidunts,</p>
  </div>

</div>
</body>
</html>
```